CD Cover Design Project (Contemporary Country Album)

I am a country singer/songwriter in need of an album cover design (front/back/inside/CD) for my self-titled Nashville-recorded debut-EP release. My musical style is contemporary country/crossover so I want something that has the look and feel of current male country artist album covers (think Wade Tolliver, Casey Brandwell, Trent Halloway, etc.).

I have attached several photos and a rough mix of the leading track. The CD template can be downloaded here:

http://www.pressvoltaire.example/templates/ecowallets.asp# (4 Panel Leaf-Sleeve w/ Spine. Jewel Box Size (W139))

I will let you apply your vision (although I do think a more serious look, rather than the one pic where I am smiling, would be best suited for the cover). As mentioned, the album will be self-titled, as "Danny Hollister".

I really want the album design to show clearly who I am (may need to crop the pictures that are further away) as this will be going to publishing/record companies, etc. The track order for the back and inside is as follows:

1) Tailwind (Copper Meadow style, song about meeting someone who is in a relationship) - this is the first track and is kind of the feel that should be reflected on at least the main cover

2) Summer Roads We Drove (uptempo song about a girl)

3) Counting Miles Between (crossover, about a long distance relationship)

4) Harbor Nights (Earl Pickens style country song)

5) Twirl (uptempo, fun party song)

Back Cover - There will need to be some room under the tracks for album credits (producer, etc.) which I will provide upon selecting a designer

Inside - The inside right cover will relist the album tracks and the smaller left panel will have some additional credits and website information (www.dannyhollister-music.example)

I hope I have provided enough direction to get the ball rolling, and look forward to seeing your responses.
Updates

A cool, blue color scheme seems to be the direction I want to go, although not too dark.  It should be contemporary, cross-over (to pop) country feel (not classic, traditional country).

Target Market(s)

Contemporary country music fans

Industry/Entity Type

Singer

Requirements
Must have
• Danny Hollister clearly written as title on cover.

Track listing on back:

1) Tailwind
2) Summer Roads We Drove
3) Counting Miles Between
4) Harbor Nights
5) Twirl

Room for Producer/songwriting credits below - details TBD once designer is selected.

Inside Right and Left Panels can be worked on once designer is selected as well.

```html
<!DOCTYPE html>
<html lang="en">
<head>
<meta charset="utf-8">
<title>Danny Hollister – Disc Label</title>
<link rel="stylesheet" href="https://fonts.googleapis.com/css2?family=Roboto:wght@700&family=Roboto+Condensed:wght@700&display=swap">
<style>
  :root {
    --page: #ffffff;
    --rim: #dfe3e6;
    --rim-edge: #b9c0c4;
    --wall-light: #4f8f8c;
    --wall-mid: #2b5d61;
    --wall-dark: #0f2429;
    --wall-moss: #6d7a3a;
    --hub: rgba(255, 255, 255, 0.32);
    --hole: #ffffff;
    --name-first: #e8a21c;
    --name-last: #f4f4f2;
    --ring-text: #f2f2f0;
  }
  html, body {
    margin: 0;
    width: 1200px;
    height: 960px;
    overflow: hidden;
    background: var(--page);
  }
  .canvas {
    position: relative;
    width: 1200px;
    height: 960px;
  }
  .disc {
    position: absolute;
    left: 0;
    top: 0;
    width: 1200px;
    height: 960px;
  }
  .disc__rim { fill: var(--rim); stroke: var(--rim-edge); stroke-width: 1.5; }
  .disc__hub { fill: var(--hub); }
  .disc__hole { fill: var(--hole); stroke: var(--rim-edge); stroke-width: 1; }
  .tracklist {
    font-family: "Roboto Condensed", "Arial Narrow", sans-serif;
    font-weight: 700;
    font-size: 17px;
    letter-spacing: 1.2px;
    fill: var(--ring-text);
  }
  .copyright {
    font-family: "Roboto Condensed", "Arial Narrow", sans-serif;
    font-weight: 700;
    font-size: 13px;
    letter-spacing: 0.8px;
    fill: var(--ring-text);
  }
  .artist-name {
    position: absolute;
    left: 192px;
    top: 410px;
    margin: 0;
    font-family: "Roboto", "Helvetica Neue", Arial, sans-serif;
    font-weight: 700;
    font-size: 58px;
    line-height: 62px;
    letter-spacing: -0.5px;
    text-transform: uppercase;
  }
  .artist-name__first { display: block; color: var(--name-first); }
  .artist-name__last { display: block; color: var(--name-last); }
</style>
</head>
<body>
<main class="canvas">
  <svg class="disc" viewBox="0 0 1200 960" xmlns="http://www.w3.org/2000/svg">
    <defs>
      <radialGradient id="wallTone" cx="42%" cy="42%" r="65%">
        <stop offset="0%" stop-color="var(--wall-light)"/>
        <stop offset="45%" stop-color="var(--wall-mid)"/>
        <stop offset="100%" stop-color="var(--wall-dark)"/>
      </radialGradient>
      <linearGradient id="mossTone" x1="0" y1="0" x2="1" y2="1">
        <stop offset="0%" stop-color="var(--wall-moss)" stop-opacity="0.35"/>
        <stop offset="50%" stop-color="var(--wall-moss)" stop-opacity="0"/>
        <stop offset="100%" stop-color="var(--wall-moss)" stop-opacity="0.2"/>
      </linearGradient>
      <path id="trackArc" d="M 381.7 122.6 A 412 412 0 1 1 740.9 859.3"/>
      <path id="copyrightArc" d="M 270.7 702.6 A 402 402 0 0 0 929.3 702.6"/>
    </defs>

    <circle class="disc__rim" cx="600" cy="472" r="441"/>
    <g role="img" aria-label="Weathered teal stone wall with a hanging iron chain">
      <circle cx="600" cy="472" r="434" fill="url(#wallTone)"/>
      <circle cx="600" cy="472" r="434" fill="url(#mossTone)"/>
    </g>

    <circle class="disc__hub" cx="600" cy="472" r="125"/>
    <circle class="disc__hole" cx="600" cy="472" r="53"/>

    <text class="tracklist">
      <textPath href="#trackArc">01. TAILWIND  02. SUMMER ROADS WE DROVE  03. COUNTING MILES BETWEEN  04. HARBOR NIGHTS  05. TWIRL</textPath>
    </text>

    <text class="copyright">
      <textPath href="#copyrightArc" startOffset="48%" text-anchor="middle">COPYRIGHT   2013 DANNY HOLLISTER  |  ALL RIGHTS RESERVED</textPath>
    </text>
  </svg>

  <h1 class="artist-name">
    <span class="artist-name__first">Danny</span>
    <span class="artist-name__last">Hollister</span>
  </h1>
</main>
</body>
</html>
```